Public Speaking Book for aspiring, ambitious speakers

I'm looking for a 6x9 book cover (Parcelo standard) as well as ebook and audiobook formats.

I'm looking for orange font on a white background as these are my brand colours.

Feel free to use some yellow and gold too if you deem it appropriate.

Title: Climb and Glow
Subtitle: Find Your Voice. Tell Your Story. Share your Message.
Author: Lionel Barstow

I would like to have a picture of a female speaker on the front cover.

Alternatively, some kind of image that symbolises public speaking like a microphone, podium etc

Target Market(s)

Aspiring professional speakers

Colors
f78f20

Requirements
Must have
• Correct spelling!
Nice to have
• A logo or picture that fits the theme, but no pressure if you can't think of anything
Should not have
• No men in suits please. I don't want this to have a 1980s corporate look.

```html
<!DOCTYPE html>
<html lang="en">
<head>
<meta charset="utf-8">
<title>Climb and Glow — Lionel Barstow</title>
<link rel="stylesheet" href="https://fonts.googleapis.com/css2?family=Bebas+Neue&family=Open+Sans:ital,wght@0,600;1,400&display=swap">
<style>
  :root {
    --paper: #efefef;
    --glow: #ffffff;
    --ink: #1e1e1c;
    --panel-white: #ffffff;
    --tone-yellow: #f5c048;
    --tone-orange: #f37a3c;
    --tone-red: #e0411a;
    --tone-green: #a6d14e;
    --tone-teal: #53c4b3;
    --tone-blue: #6fa0c6;
    --tone-pink: #d6467a;
  }
  html, body {
    margin: 0;
    padding: 0;
    width: 800px;
    height: 1200px;
    overflow: hidden;
    background: var(--paper);
  }
  .cover {
    display: block;
    width: 800px;
    height: 1200px;
  }
  .title-word {
    font-family: "Bebas Neue", "Oswald", sans-serif;
    fill: var(--ink);
  }
  .subtitle {
    font-family: "Open Sans", sans-serif;
    font-style: italic;
    font-weight: 400;
    fill: var(--ink);
  }
  .author {
    font-family: "Open Sans", sans-serif;
    font-weight: 600;
    fill: var(--ink);
  }
</style>
</head>
<body>
<svg class="cover" viewBox="0 0 800 1200" xmlns="http://www.w3.org/2000/svg" aria-label="Climb and Glow. Find Your Voice. Tell Your Story. Share your Message. By Lionel Barstow">
  <defs>
    <radialGradient id="backGlow" cx="0.5" cy="0.5" r="0.5">
      <stop offset="0" stop-color="var(--glow)"/>
      <stop offset="0.7" stop-color="var(--glow)" stop-opacity="0.8"/>
      <stop offset="1" stop-color="var(--paper)" stop-opacity="0"/>
    </radialGradient>
    <radialGradient id="groundShadow" cx="0.5" cy="0.5" r="0.5">
      <stop offset="0" stop-color="#b9bcc0" stop-opacity="0.8"/>
      <stop offset="1" stop-color="#b9bcc0" stop-opacity="0"/>
    </radialGradient>
    <linearGradient id="artTones" x1="0" y1="0" x2="1" y2="1">
      <stop offset="0" stop-color="var(--tone-green)"/>
      <stop offset="0.3" stop-color="var(--tone-yellow)"/>
      <stop offset="0.6" stop-color="var(--tone-orange)"/>
      <stop offset="1" stop-color="var(--tone-pink)"/>
    </linearGradient>
  </defs>

  <rect class="background" width="800" height="1200" fill="var(--paper)"/>
  <ellipse class="background-glow" cx="400" cy="840" rx="360" ry="330" fill="url(#backGlow)"/>

  <g class="title">
    <text class="title-word title-climb" x="166" y="314" font-size="372" textLength="466" lengthAdjust="spacingAndGlyphs">CLIMB</text>
    <text class="title-word title-and" x="339" y="408" font-size="103" textLength="124" lengthAdjust="spacingAndGlyphs">AND</text>
    <text class="title-word title-glow" x="167" y="578" font-size="207" textLength="466" lengthAdjust="spacingAndGlyphs">GLOW</text>
  </g>

  <rect class="speech-art" x="130" y="612" width="535" height="435" rx="200" fill="url(#artTones)" opacity="0.7" role="img" aria-label="Illustration of many overlapping colourful speech bubbles"/>
  <ellipse class="ground-shadow" cx="410" cy="1072" rx="200" ry="10" fill="url(#groundShadow)"/>

  <g class="subtitle-panel">
    <ellipse cx="398" cy="829" rx="162" ry="108" fill="var(--panel-white)"/>
    <text class="subtitle" text-anchor="middle" font-size="27">
      <tspan x="398" y="795">Find Your Voice.</tspan>
      <tspan x="398" y="838">Tell Your Story.</tspan>
      <tspan x="398" y="881">Share your Message.</tspan>
    </text>
  </g>

  <text class="author" x="400" y="1155" text-anchor="middle" font-size="56">Lionel Barstow</text>
</svg>
</body>
</html>
```